International Consultancy Needs Slick Professional Presentation Graphic

Varnolt are an international engineering and advisory consultancy servicing the mining industry with a mix of Technology (Software), Services (consulting) and Systems (work structures).

We need a slick presentation graphic for use in presentation slides, whitepapers. I have attached a basic pic of the information we want to convey. Flat or 3D no preference, colouring no preference. Don't have to be circles, that was just easiest to draft up initially.

Industry/Entity Type

Mining

```html
<!DOCTYPE html>
<html lang="en">
<head>
<meta charset="utf-8">
<title>Varnolt Capability Model</title>
<link rel="stylesheet" href="https://fonts.googleapis.com/css2?family=Jost:wght@400;700&display=swap">
<style>
  :root {
    --bg: #ffffff;
    --systems: #2fd67e;
    --technology: #42c7eb;
    --people: #2a7fe6;
    --sys-tech: #14b55e;
    --sys-people: #0c6b7b;
    --tech-people: #1459e2;
    --core: #ebe9e6;
    --core-text: #6a0f1f;
    --banner-systems: #2b6fe0;
    --banner-technology: #2fc47b;
    --banner-people: #43c1e2;
    --banner-fold: #111111;
    --label: #ffffff;
  }
  html, body {
    margin: 0;
    padding: 0;
    width: 1200px;
    height: 829px;
    overflow: hidden;
    background: var(--bg);
  }
  .capability-model {
    display: block;
    width: 1200px;
    height: 829px;
  }
  .capability-model text {
    font-family: "Jost", "Futura", sans-serif;
    text-anchor: middle;
    dominant-baseline: middle;
  }
  .circle-systems { fill: var(--systems); }
  .circle-technology { fill: var(--technology); }
  .circle-people { fill: var(--people); }
  .overlap-sys-tech { fill: var(--sys-tech); }
  .overlap-sys-people { fill: var(--sys-people); }
  .overlap-tech-people { fill: var(--tech-people); }
  .overlap-core { fill: var(--core); }
  .banner-systems { fill: var(--banner-systems); }
  .banner-technology { fill: var(--banner-technology); }
  .banner-people { fill: var(--banner-people); }
  .banner-fold { fill: var(--banner-fold); }
  .banner-title {
    fill: var(--label);
    font-weight: 700;
    font-size: 37px;
    filter: url(#text-shadow);
  }
  .overlap-label {
    fill: var(--label);
    font-weight: 400;
    font-size: 23px;
    filter: url(#text-shadow);
  }
  .core-label {
    fill: var(--core-text);
    font-weight: 700;
    font-size: 50px;
  }
</style>
</head>
<body>
<svg class="capability-model" viewBox="0 0 1200 829" xmlns="http://www.w3.org/2000/svg" role="img" aria-label="Capability at the intersection of Systems, Technology and People">
  <defs>
    <clipPath id="clip-systems"><circle cx="593" cy="302" r="290"/></clipPath>
    <clipPath id="clip-technology"><circle cx="482" cy="522" r="290"/></clipPath>
    <clipPath id="clip-people"><circle cx="705" cy="522" r="290"/></clipPath>
    <filter id="text-shadow" x="-20%" y="-40%" width="140%" height="180%">
      <feDropShadow dx="1" dy="2" stdDeviation="2" flood-color="#000" flood-opacity="0.55"/>
    </filter>
  </defs>

  <!-- Circles -->
  <circle class="circle-technology" cx="482" cy="522" r="290"/>
  <circle class="circle-people" cx="705" cy="522" r="290"/>
  <circle class="circle-systems" cx="593" cy="302" r="290"/>

  <!-- Pairwise overlaps -->
  <g clip-path="url(#clip-systems)">
    <circle class="overlap-sys-tech" cx="482" cy="522" r="290"/>
  </g>
  <g clip-path="url(#clip-systems)">
    <circle class="overlap-sys-people" cx="705" cy="522" r="290"/>
  </g>
  <g clip-path="url(#clip-technology)">
    <circle class="overlap-tech-people" cx="705" cy="522" r="290"/>
  </g>

  <!-- Core overlap -->
  <g clip-path="url(#clip-systems)">
    <g clip-path="url(#clip-technology)">
      <circle class="overlap-core" cx="705" cy="522" r="290"/>
    </g>
  </g>

  <!-- Banners -->
  <g class="banner banner--systems">
    <polygon class="banner-fold" points="272,204 310,204 310,214"/>
    <polygon class="banner-fold" points="912,204 874,204 874,214"/>
    <rect class="banner-systems" x="272" y="126" width="640" height="78"/>
    <text class="banner-title" x="592" y="167">Systems</text>
  </g>
  <g class="banner banner--technology">
    <polygon class="banner-fold" points="137,616 205,616 205,628"/>
    <rect class="banner-technology" x="137" y="538" width="231" height="78"/>
    <text class="banner-title" x="253" y="579">Technology</text>
  </g>
  <g class="banner banner--people">
    <polygon class="banner-fold" points="1045,616 985,616 985,628"/>
    <rect class="banner-people" x="815" y="538" width="230" height="78"/>
    <text class="banner-title" x="930" y="579">People</text>
  </g>

  <!-- Overlap labels -->
  <text class="overlap-label" x="394" y="323">System</text>
  <text class="overlap-label" x="394" y="350">Interface</text>
  <text class="overlap-label" x="394" y="377">Engineering</text>

  <text class="overlap-label" x="772" y="337">Organisation</text>
  <text class="overlap-label" x="772" y="363">Design</text>

  <text class="overlap-label" x="591" y="656">User Interface</text>
  <text class="overlap-label" x="591" y="682">Engineering</text>

  <text class="core-label" x="590" y="466">Capability</text>
</svg>
</body>
</html>
```